Vantrell Law Letterhead

We need a new letterhead design for a Law Firm. The address for the law firm is 4817 Larkspur Boulevard, Suite 250, Houston, Texas 77342. Phone Number: 832-619-3057; Fax Number: 832-407-1694. The logo is uploaded to the project.

```html
<!DOCTYPE html>
<html lang="en">
<head>
<meta charset="utf-8">
<title>Vantrell Law Letterhead</title>
<link rel="stylesheet" href="https://fonts.googleapis.com/css2?family=Cinzel:wght@500&family=Arimo:wght@400&display=swap">
<style>
  :root {
    --navy: #1d3264;
    --red: #e01b24;
    --red-dark: #6c0a10;
    --text: #4a4a4a;
    --rule: #6b6b6b;
    --paper: #ffffff;
  }
  html, body {
    margin: 0;
    padding: 0;
    overflow: hidden;
    background: var(--paper);
  }
  .letterhead {
    position: relative;
    width: 848px;
    height: 1200px;
    background: var(--paper);
    overflow: hidden;
  }
  .brand {
    position: absolute;
    left: 47px;
    top: 66px;
    display: flex;
    align-items: center;
    gap: 16px;
  }
  .brand-mark {
    width: 52px;
    height: 52px;
    background: var(--navy);
  }
  .brand-name {
    font-family: "Cinzel", serif;
    font-weight: 500;
    font-size: 40px;
    letter-spacing: 0.5px;
    color: var(--navy);
    margin: 0;
    line-height: 1;
  }
  .contact {
    position: absolute;
    top: 80px;
    left: 445px;
    display: flex;
    font-family: "Arimo", sans-serif;
    font-style: normal;
    font-size: 14.5px;
    color: var(--text);
  }
  .contact-group {
    border-left: 1px solid var(--rule);
    padding: 0 7px 0 8px;
    display: flex;
    flex-direction: column;
    gap: 7px;
    line-height: 16px;
  }
  .contact-line {
    display: flex;
    align-items: center;
    gap: 5px;
    white-space: nowrap;
  }
  .contact-icon {
    width: 15px;
    height: 15px;
    fill: var(--navy);
  }
  .footer-band {
    position: absolute;
    left: 0;
    bottom: 0;
    width: 848px;
    height: 90px;
    background:
      linear-gradient(180deg, var(--navy) 0 14px, transparent 14px),
      linear-gradient(90deg, var(--red-dark), var(--red));
  }
</style>
</head>
<body>
<main class="letterhead">
  <header>
    <div class="brand">
      <span class="brand-mark" aria-hidden="true"></span>
      <h1 class="brand-name">Vantrell Law</h1>
    </div>
    <address class="contact">
      <div class="contact-group">
        <span class="contact-line">
          <svg class="contact-icon" viewBox="0 0 24 24" aria-label="Phone"><path d="M6.6 10.8a15.1 15.1 0 0 0 6.6 6.6l2.2-2.2c.3-.3.7-.4 1-.2 1.1.4 2.3.6 3.6.6.6 0 1 .4 1 1V20c0 .6-.4 1-1 1C10.6 21 3 13.4 3 4c0-.6.4-1 1-1h3.5c.6 0 1 .4 1 1 0 1.3.2 2.5.6 3.6.1.3 0 .7-.2 1z"/></svg>
          832-619-3057
        </span>
        <span class="contact-line">
          <svg class="contact-icon" viewBox="0 0 24 24" aria-label="Fax"><path d="M7 2h10v6H7z M3 9h18a1 1 0 0 1 1 1v10a1 1 0 0 1-1 1H3a1 1 0 0 1-1-1V10a1 1 0 0 1 1-1zm3 4v2h12v-2z"/></svg>
          832-407-1694
        </span>
      </div>
      <div class="contact-group">
        <span class="contact-line">4817 Larkspur Boulevard</span>
        <span class="contact-line">Suite 250, Houston, Texas 77342</span>
      </div>
    </address>
  </header>

  <div class="footer-band" role="img" aria-label="Decorative navy and red footer band"></div>
</main>
</body>
</html>
```